Web Site for Strategy and Technology Consulting Company

We are looking for a website design that engages potential customers to understand our services and contact us. In this contest, we are looking for a homepage design, but the winning designer will be favored for the design of some of the more complicated interior pages of the site. An additional contest (or contests) for these pages will be added soon.

PLATROM AND RESPONSIVE DESIGN
The site will be implemented in WordPress using the Elementor page builder.
We are looking for a design that will look good on phones are well as laptop browsers.

UPLOADED FILES INCLUDE:
1a A wireframe of the homepage we are looking for. The Uploaded PDF also includes a draft of the text proposed for the homepage. Designers are free to go beyond the wireframe, but all elements of the wireframe should be included.
1b A Word document with the draft text of the homepage.
2a-d The Norvalith logo. Two versions are included – a dark version which works well against a light background, and a light version which works well against a dark background.
3 The Norvalith color palette with HEX and RGB values. Designers are not limited to this palette, but colors should be complementary.
4 A draft of the homepage menu
5 Service sheets with information on the services we provide

MORE ABOUT NORVALITH
Norvalith is a consulting company focused on transforming businesses through software. Our tagline, “Transformation Delivered,” recognizes the gap business often have between business transformation and the software they end up with. By listening to our customers and understanding their vision and where they are, we help get our customers where they want to go.

We increase our capability by working with many consultants and partners, allowing us to provide our customers with the best people and the software that best suits them.

Industry/Entity Type

Consulting

Number of Pages Required

1 page

Font styles to use
Sans Serif

Requirements
Must have
• the content represented on the wireframe uploaded
Nice to have
• interactive features, such as roll-over icons that reveal additional information

```html
<!DOCTYPE html>
<html lang="en">
<head>
<meta charset="utf-8">
<title>Norvalith — Transformation Delivered</title>
<link href="https://fonts.googleapis.com/css2?family=Plus+Jakarta+Sans:wght@500;600;700&family=Poppins:wght@300;400;500&display=swap" rel="stylesheet">
<style>
:root{
  --brand:#215f94;
  --brand-dark:#1b4f7d;
  --ink:#3c4a5c;
  --body:#5d6673;
  --soft:#eef4fb;
  --line:#c9d6e4;
  --tick:#b9d2ea;
  --white:#ffffff;
}
*{margin:0;padding:0;box-sizing:border-box}
html,body{width:1200px;height:3290px;overflow:hidden;background:var(--white)}
body{font-family:"Poppins",sans-serif;color:var(--body);position:relative}
h1,h2,h3,h4{font-family:"Plus Jakarta Sans",sans-serif}
section,header,footer{position:relative;width:1200px}
.abs{position:absolute}

/* hero */
.hero{height:633px;overflow:hidden}
.hero-photo{position:absolute;inset:0;background:linear-gradient(160deg,#6d94bd 0%,#4f7cab 40%,#3f6e9f 100%)}
.nav{position:absolute;left:108px;right:108px;top:10px;height:42px;display:flex;align-items:center}
.brand{font-family:"Plus Jakarta Sans",sans-serif;font-weight:500;color:var(--white);font-size:36px;letter-spacing:-.5px}
.nav-links{margin-left:auto;display:flex;gap:28px;align-items:center;font-size:14px;color:var(--white);font-weight:500}
.nav-cta{border:1px solid var(--white);border-radius:4px;padding:8px 12px;margin-left:14px}
.hero h1{position:absolute;top:192px;width:100%;text-align:center;color:var(--white);font-size:52px;line-height:64px;font-weight:700;letter-spacing:-.5px}
.hero-sub{position:absolute;top:338px;width:100%;text-align:center;color:var(--white);font-size:15px}
.btn-light{position:absolute;left:532px;top:400px;width:136px;height:42px;background:var(--white);color:var(--brand);border-radius:4px;font-size:13px;font-weight:500;display:flex;align-items:center;justify-content:center}

.btn{display:flex;align-items:center;justify-content:center;background:var(--brand);color:var(--white);border-radius:4px;font-size:13px;font-weight:500}

/* delivered */
.delivered{height:640px}
.delivered h2{left:108px;top:76px;font-size:35px;color:var(--ink);font-weight:600}
.copy{font-size:13.3px;line-height:20px;color:var(--body)}
.ticks{list-style:none}
.ticks li{display:flex;gap:12px;align-items:center;margin-bottom:13px}
.tick{flex:0 0 20px;height:20px;border-radius:50%;background:var(--tick);display:flex;align-items:center;justify-content:center}
.team-photo{left:775px;top:92px;width:425px;height:424px;border-radius:14px 0 0 14px;background:linear-gradient(135deg,#6f8fb4,#3e6a9a 60%,#2b5686)}

/* technology */
.tech{height:739px}
.center{left:0;width:100%;text-align:center}
.nowrap{white-space:nowrap}
.tech h2{top:45px;font-size:35px;line-height:41px;color:var(--ink);font-weight:600}
.cards{left:108px;top:310px;display:flex;gap:10px}
.card{width:189px;height:219px;border:1.5px solid var(--line);border-radius:6px;padding:12px 13px}
.card h3{font-size:15px;line-height:22px;color:var(--brand-dark);font-weight:600;margin-top:8px}
.card p{font-size:13px;line-height:20px;margin-top:4px}

/* people */
.people{height:469px}
.people h2{left:608px;top:37px;font-size:35px;color:var(--ink);font-weight:600}
.panel{border-radius:8px}
.feature{display:flex;gap:12px;align-items:flex-start;margin-bottom:16px}
.feature-icon{flex:0 0 32px;height:32px;border-radius:6px;background:#d3e4f4;display:flex;align-items:center;justify-content:center}

/* reviews */
.reviews{height:413px;background:var(--soft)}
.reviews h2{top:75px;font-size:35px;color:var(--ink);font-weight:600}
.review-row{left:108px;top:156px;display:flex;gap:9px}
.review{width:322px;height:146px;background:var(--white);border-radius:8px;padding:18px 13px}
.review p{font-size:13px;line-height:16.5px}
.review h3{font-size:15px;color:var(--ink);font-weight:600;margin-top:13px}
.review span{font-size:11px}
.dots{left:574px;top:334px;display:flex;gap:7px}
.dots i{width:8px;height:8px;border-radius:50%;background:#a8bfd6}
.dots i.on{background:var(--brand)}

/* footer */
.site-footer{height:396px;background:var(--brand);color:#cfe0f1}
.site-footer .brand{font-size:54px;left:108px;top:84px;position:absolute}
.foot-col h4{color:var(--white);font-size:15px;font-weight:600;margin-bottom:16px}
.foot-col a{display:block;font-size:13px;color:#b9d1ea;text-decoration:none;margin-bottom:9px}
.social{display:flex;gap:11px}
.social i{width:33px;height:33px;border-radius:50%;background:var(--white)}
.copyright{left:108px;top:347px;font-size:10px;color:#cfe0f1}
</style>
</head>
<body>

<header class="hero">
  <div class="hero-photo" role="img" aria-label="Glass office tower photographed from below, tinted blue"></div>
  <nav class="nav">
    <span class="brand">Norvalith</span>
    <div class="nav-links">
      <span>About Us</span>
      <span>Services <svg width="10" height="6" viewBox="0 0 10 6"><path d="M1 1l4 4 4-4" stroke="#fff" fill="none"/></svg></span>
      <span>Insights</span>
      <span>Join Us</span>
      <span class="nav-cta">Contact Us</span>
    </div>
  </nav>
  <h1>Transform Your Business with<br>Proven Consulting Strategies</h1>
  <p class="hero-sub">Streamline Operations and Maximize Efficiency with Professional Consulting</p>
  <a class="btn-light">Get Started</a>
</header>

<section class="delivered">
  <h2 class="abs">Transformation Delivered</h2>
  <div class="abs copy" style="left:108px;top:148px;width:555px">
    <p>We do more for our customers than implement software. We listen. We work to understand where they are in their transformation journey and where they want to go. We partner with them to clear the roadblocks that stand in their way, ensuring they reach their destination.</p>
    <p style="margin-top:20px">At Norvalith, we:</p>
    <ul class="ticks" style="margin-top:20px">
      <li><span class="tick"><svg width="10" height="8" viewBox="0 0 10 8"><path d="M1 4l3 3 5-6" stroke="#215f94" stroke-width="1.6" fill="none"/></svg></span>Focus on business value, with an emphasis on delivering value quickly.</li>
      <li><span class="tick"><svg width="10" height="8" viewBox="0 0 10 8"><path d="M1 4l3 3 5-6" stroke="#215f94" stroke-width="1.6" fill="none"/></svg></span>Meet our customers where they are without backing them up to<br>the beginning of their journey.</li>
      <li><span class="tick"><svg width="10" height="8" viewBox="0 0 10 8"><path d="M1 4l3 3 5-6" stroke="#215f94" stroke-width="1.6" fill="none"/></svg></span>Provide a wide range of services, from strategy to product support.</li>
      <li><span class="tick"><svg width="10" height="8" viewBox="0 0 10 8"><path d="M1 4l3 3 5-6" stroke="#215f94" stroke-width="1.6" fill="none"/></svg></span>Commit to our customer’s long-term success.</li>
    </ul>
    <p style="margin-top:18px">Norvalith is business transformation, delivered.</p>
  </div>
  <a class="abs btn" style="left:108px;top:490px;width:123px;height:43px">Our Story</a>
  <div class="abs team-photo" role="img" aria-label="Three colleagues in business attire reviewing a tablet together"></div>
</section>

<section class="tech">
  <h2 class="abs center">Transformation Supported<br>by Technology</h2>
  <p class="abs center copy nowrap" style="top:139px">During our early years, Norvalith focused only on business transformation. We came to realize that successful<br>transformation often depended on quality software implementations, and often more than one. Now we focus on five<br>things, the five things most businesses need to reach their goals.</p>
  <a class="abs btn" style="left:524px;top:226px;width:152px;height:43px">How We Work</a>
  <div class="abs cards">
    <div class="card">
      <svg width="56" height="56" viewBox="0 0 56 56" fill="none" stroke="#215f94" stroke-width="1.6"><path d="M4 4l6 6M10 4l-6 6M4 44l6 6M10 44l-6 6M44 24l6 6M50 24l-6 6M26 44l6 6M32 44l-6 6"/><path d="M8 36v-8h22V10h10"/><circle cx="48" cy="10" r="4"/><circle cx="8" cy="40" r="3"/></svg>
      <h3>Business<br>Transformation</h3>
      <p>Define and execute your strategy.</p>
    </div>
    <div class="card">
      <svg width="56" height="56" viewBox="0 0 56 56" fill="none" stroke="#215f94" stroke-width="1.6"><rect x="4" y="4" width="48" height="38" rx="2"/><path d="M4 10h48M20 50h16M28 42v8"/><circle cx="36" cy="26" r="8"/><circle cx="36" cy="26" r="3"/><path d="M10 18h12M10 24h10M10 30h12"/></svg>
      <h3>ERP<br>Implementations</h3>
      <p>Assess, upgrade, and implement ERP solutions to meet your needs.</p>
    </div>
    <div class="card">
      <svg width="56" height="56" viewBox="0 0 56 56" fill="none" stroke="#1f2a37" stroke-width="1.8"><circle cx="14" cy="12" r="8"/><circle cx="42" cy="12" r="8"/><circle cx="28" cy="42" r="8"/><path d="M20 18l4 16M36 18l-4 16M22 12h12"/><circle cx="28" cy="28" r="5" stroke="#215f94"/></svg>
      <h3>CRM<br>Implementations</h3>
      <p>Take your relationships to the next level.</p>
    </div>
    <div class="card">
      <svg width="56" height="56" viewBox="0 0 56 56" fill="none" stroke="#215f94" stroke-width="1.6"><rect x="4" y="4" width="48" height="48" rx="2"/><path d="M4 10h48"/><circle cx="16" cy="22" r="6"/><path d="M16 16v6h6M30 18h16M30 24h12"/><path d="M10 46v-6M16 46v-8M22 46v-4M28 46v-10M34 46v-6M40 46v-8M46 46v-10"/></svg>
      <h3>BI and Data</h3>
      <p>Discover, connect, and trust your data.</p>
    </div>
    <div class="card">
      <svg width="56" height="56" viewBox="0 0 56 56" fill="none" stroke="#215f94" stroke-width="1.6"><rect x="10" y="4" width="34" height="46" rx="2"/><path d="M14 54h34V10"/><circle cx="27" cy="24" r="9"/><circle cx="27" cy="22" r="3"/><path d="M22 30c2-3 8-3 10 0M16 40h22M16 45h16"/></svg>
      <h3>Building the Right<br>Team of People</h3>
      <p>Hire resources for your transformation journey.</p>
    </div>
  </div>
  <p class="abs center copy" style="top:570px">Find out how Norvalith can help you put all the pieces together and get them done.</p>
</section>

<section class="people">
  <div class="abs panel" style="left:108px;top:0;width:400px;height:188px;background:linear-gradient(180deg,#4e7aa8,#2b5383)" role="img" aria-label="Silhouettes of a team meeting in a glass boardroom above the city"></div>
  <div class="abs panel" style="left:108px;top:202px;width:193px;height:192px;background:linear-gradient(135deg,#9bb3cf,#6a8db6)" role="img" aria-label="Hands typing on a laptop keyboard at a desk"></div>
  <div class="abs panel" style="left:315px;top:202px;width:193px;height:192px;background:var(--brand);color:var(--white)">
    <div class="abs" style="left:52px;top:76px;font-family:'Plus Jakarta Sans',sans-serif;font-weight:600;font-size:17px">Learn More</div>
    <svg class="abs" style="left:53px;top:100px" width="20" height="16" viewBox="0 0 20 16" fill="none" stroke="#fff" stroke-width="1.5"><path d="M2 1v8h15M13 5l4 4-4 4"/></svg>
  </div>
  <h2 class="abs">It’s the People</h2>
  <div class="abs copy" style="left:608px;top:106px;width:484px">
    <p>The world has changed in the past twenty years. The people you need might not all work for one company. Our clients want the best resources, available quickly. That’s why, in addition to our team of experts, we partner with:</p>
    <div style="margin-top:20px">
      <div class="feature"><span class="feature-icon"><svg width="18" height="18" viewBox="0 0 18 18" fill="#215f94"><circle cx="9" cy="9" r="2.5"/><circle cx="3" cy="3" r="1.8"/><circle cx="15" cy="3" r="1.8"/><circle cx="3" cy="15" r="1.8"/><circle cx="15" cy="15" r="1.8"/><path d="M3 3l12 12M15 3L3 15" stroke="#215f94" stroke-width="1"/></svg></span><span>A large network of expert consultants who are the<br>best at what they do.</span></div>
      <div class="feature"><span class="feature-icon"><svg width="20" height="18" viewBox="0 0 20 18" fill="none" stroke="#215f94" stroke-width="1.4"><path d="M3 10a7 7 0 0 1 14 0"/><rect x="1.5" y="9" width="3" height="5" rx="1"/><rect x="15.5" y="9" width="3" height="5" rx="1"/></svg></span><span>Service providers all over the world to provide the resources<br>and value that are right for you, available 24 x 7.</span></div>
    </div>
    <p style="margin-top:6px">People are invariably at the center of our customer’s success. Find out how we can add our experts to yours.</p>
  </div>
</section>

<section class="reviews">
  <h2 class="abs center">Reviews from Our Satisfied Clients</h2>
  <div class="abs review-row">
    <div class="review"><p>“Lorem ipsum dolor sit amet consectetur. In purus vulputate arcu eget ullamcorper fames. Sodales malesuada vestibulum amet ac arcu volutpat viverra.”</p><h3>Evan Marsh</h3><span>CEO Brightmoor</span></div>
    <div class="review"><p>“Lorem ipsum dolor sit amet consectetur. In purus vulputate arcu eget ullamcorper fames. Sodales malesuada vestibulum amet ac arcu volutpat viverra.”</p><h3>Clara Venn</h3><span>COO Quillstream</span></div>
    <div class="review"><p>“Lorem ipsum dolor sit amet consectetur. In purus vulputate arcu eget ullamcorper fames. Sodales malesuada vestibulum amet ac arcu volutpat viverra.”</p><h3>Iris Dalton</h3><span>CMO Lumenhall</span></div>
  </div>
  <div class="abs dots"><i class="on"></i><i></i><i></i><i></i></div>
</section>

<footer class="site-footer">
  <span class="brand">Norvalith</span>
  <div class="abs foot-col" style="left:608px;top:88px">
    <h4>Quick Links</h4>
    <a>About Us</a><a>Services</a><a>Insights</a><a>Join Us</a>
  </div>
  <div class="abs foot-col" style="left:758px;top:88px">
    <h4>Company</h4>
    <a>Blog</a><a>Terms and Conditions</a><a>Privacy Policy</a><a>Career</a><a>Contact</a>
  </div>
  <div class="abs foot-col" style="left:971px;top:88px">
    <h4>Social Media</h4>
    <div class="social"><i></i><i></i><i></i></div>
  </div>
  <p class="abs copyright">©Norvalith 2023</p>
</footer>

</body>
</html>
```